Plantwise Mechanics Partners. Needs a Business Card Design

We need a business card design for an engineering company which supplies industrial components (pumps, compressors, mechanical seals) provides repairs and services for above mentioned equipments. We offer a uniqe engineering solutions which help our customers to increase the productivness of their manufacturings, and energy savings.

Target Market(s)

Chemical and energy plants, refineries. Food industry and private consumers in a less.

Industry/Entity Type

Business

Contact Information for Business Card

Stylish and sleek design oriented on industrial area.

Requirements
Should not have
• company name shortening

```html
<!DOCTYPE html>
<html lang="en">
<head>
<meta charset="utf-8">
<title>Plantwise Mechanics Partners – Business Card</title>
<link rel="stylesheet" href="https://fonts.googleapis.com/css2?family=Source+Sans+3:wght@400;600;700&display=swap">
<style>
  :root {
    --stage: #3b4249;
    --brand-blue: #1f3c9c;
    --brand-blue-light: #2a4cb3;
    --brand-red: #ee3a2c;
    --paper: #ffffff;
    --ink-grey: #7d7d7d;
    --white: #ffffff;
  }
  * { margin: 0; padding: 0; box-sizing: border-box; }
  html, body {
    width: 1200px; height: 960px; overflow: hidden;
    background: var(--stage);
    font-family: "Source Sans 3", "Myriad Pro", sans-serif;
  }
  .stage { position: relative; width: 1200px; height: 960px; }
  .card {
    position: absolute; left: 250px; width: 700px; height: 400px;
    overflow: hidden; border-radius: 2px;
    box-shadow: 0 10px 30px rgba(0,0,0,.35);
  }

  /* Front */
  .card-front { top: 60px; background: var(--brand-blue); color: var(--white); }
  .front-brand {
    position: absolute; top: 130px; left: 0; width: 100%;
    display: flex; flex-direction: column; align-items: center; gap: 14px;
  }
  .brand-dot { width: 56px; height: 56px; border-radius: 50%; background: var(--brand-red); }
  .front-name { font-size: 40px; font-weight: 700; letter-spacing: .3px; }
  .front-web { position: absolute; top: 300px; width: 100%; text-align: center; font-size: 17px; }

  /* Back */
  .card-back { top: 500px; background: var(--paper); }
  .back-brand {
    position: absolute; top: 44px; left: 48px;
    display: flex; align-items: center; gap: 14px;
  }
  .back-brand .brand-dot { width: 42px; height: 42px; }
  .back-brand-name { font-size: 28px; font-weight: 700; color: var(--brand-blue); }
  .person { position: absolute; top: 126px; left: 48px; }
  .person-name { font-size: 27px; font-weight: 700; color: var(--brand-blue); line-height: 1.1; }
  .person-title { font-size: 19px; color: var(--ink-grey); }
  .wave { position: absolute; inset: 0; }
  .social {
    position: absolute; top: 318px; left: 60px;
    display: flex; align-items: center; gap: 10px;
    color: var(--white); font-size: 19px;
  }
  .social-dot { width: 14px; height: 14px; border-radius: 50%; background: #f5a623; }
  .contact { position: absolute; top: 112px; right: 44px; text-align: right; }
  .contact-company { font-size: 20px; color: var(--brand-red); font-weight: 600; }
  .contact-address { font-size: 18px; color: var(--ink-grey); line-height: 1.25; margin-bottom: 14px; }
  .contact-line {
    display: flex; justify-content: flex-end; align-items: center; gap: 12px;
    font-size: 18px; color: var(--ink-grey); line-height: 1.4;
  }
  .contact-line svg { width: 18px; height: 18px; flex: none; }
</style>
</head>
<body>
<main class="stage">

  <section class="card card-front" aria-label="Business card front">
    <div class="front-brand">
      <span class="brand-dot"></span>
      <span class="front-name">Plantwise Mechanics Partners</span>
    </div>
    <p class="front-web">www.plantwisemechanics.com</p>
  </section>

  <section class="card card-back" aria-label="Business card back">
    <svg class="wave" viewBox="0 0 700 400" preserveAspectRatio="none" aria-hidden="true">
      <path d="M0 282 C160 262 300 292 420 350 C500 388 600 400 700 392 L700 400 L0 400 Z" fill="var(--brand-blue)"/>
      <path d="M0 282 C160 262 280 286 360 316 C260 290 140 284 0 298 Z" fill="var(--brand-blue-light)"/>
      <path d="M430 318 C530 352 620 360 700 352 L700 374 C610 380 520 366 430 318 Z" fill="var(--brand-red)"/>
    </svg>

    <div class="back-brand">
      <span class="brand-dot"></span>
      <span class="back-brand-name">Plantwise Mechanics Partners</span>
    </div>

    <div class="person">
      <p class="person-name">Daniel Morrow</p>
      <p class="person-title">President &amp; CEO</p>
    </div>

    <div class="contact">
      <p class="contact-company">Plantwise Mechanics Partners</p>
      <p class="contact-address">Suite 123 Street Name<br>State, Zip 1234, Country</p>
      <p class="contact-line">(123) 456.7890
        <svg viewBox="0 0 24 24"><path d="M6 3h4l2 5-3 2a11 11 0 0 0 5 5l2-3 5 2v4a2 2 0 0 1-2 2A17 17 0 0 1 4 5a2 2 0 0 1 2-2z" fill="var(--brand-red)"/></svg>
      </p>
      <p class="contact-line">(123) 456.7890
        <svg viewBox="0 0 24 24"><rect x="6" y="3" width="12" height="5" fill="var(--brand-red)"/><rect x="3" y="9" width="18" height="8" rx="1" fill="var(--brand-red)"/><rect x="7" y="14" width="10" height="7" fill="var(--brand-red)" stroke="#fff" stroke-width="1.5"/></svg>
      </p>
      <p class="contact-line">info@plantwisemechanics.com
        <svg viewBox="0 0 24 24"><rect x="3" y="5" width="18" height="14" fill="none" stroke="var(--brand-red)" stroke-width="2"/><path d="M3 5l9 8 9-8" fill="none" stroke="var(--brand-red)" stroke-width="2"/></svg>
      </p>
      <p class="contact-line">www.plantwisemechanics.com
        <svg viewBox="0 0 24 24"><g fill="none" stroke="var(--brand-red)" stroke-width="1.8"><circle cx="12" cy="12" r="9"/><ellipse cx="12" cy="12" rx="4" ry="9"/><path d="M3 12h18M5 7h14M5 17h14"/></g></svg>
      </p>
    </div>

    <div class="social">
      <span class="social-dot"></span>
      <span>@PlantwiseMech</span>
    </div>
  </section>

</main>
</body>
</html>
```